VELMIT Business Card

VELMIT (www.velmitpools.example) is a veteran in the swimming pool maintenance and repair business..we have served our clients for 15 years and have a research chemist, an electrician, a plumber and a pool building contractor (in part) on staff...We want to provide a business card that has a dual purpose, that people want to keep around, that leaves people speechless in the sense that they understand the mission of and the experience level of the TEAM at VELMIT.

Target Market(s)

persons who enjoy swimming and make it a priority to swim

Industry/Entity Type

Building

Font styles to use
Serif
Sans Serif

Colors
85acd3
3176b5
95b6d8
3276b5
0355a3
0555a3
0255a3
0455a3
85abd2

Requirements
Must have
• name, title, address, email, text
Nice to have
• a die cut shape
Should not have
• cartoons, pictures of pools

```html
<!DOCTYPE html>
<html lang="en">
<head>
<meta charset="utf-8">
<title>VELMIT Business Card</title>
<link href="https://fonts.googleapis.com/css2?family=Montserrat:wght@300;400;600&display=swap" rel="stylesheet">
<style>
  :root {
    --page: #eef1f5;
    --blue-deep: #0355a3;
    --blue-mid: #3176b5;
    --blue-light: #85acd3;
    --blue-pale: #95b6d8;
    --white: #ffffff;
    --band: #eef0f3;
    --map-tone: #dde3ea;
  }
  * { box-sizing: border-box; margin: 0; padding: 0; }
  html, body { width: 1200px; height: 724px; overflow: hidden; }
  body {
    background: var(--page);
    font-family: "Montserrat", sans-serif;
    position: relative;
  }
  .card {
    position: absolute;
    top: 72px;
    width: 340px;
    height: 580px;
    overflow: hidden;
    box-shadow: 0 6px 20px rgba(3, 85, 163, 0.18);
  }
  .card--front { left: 230px; background: linear-gradient(160deg, var(--blue-light) 0%, var(--blue-mid) 55%, var(--blue-deep) 100%); }
  .card--back  { left: 630px; background: linear-gradient(160deg, var(--blue-pale) 0%, var(--blue-mid) 60%, var(--blue-deep) 100%); }

  /* front */
  .brand-disc {
    position: absolute; left: 85px; top: 60px;
    width: 170px; height: 170px; border-radius: 50%;
    background: var(--white);
    box-shadow: 0 0 0 8px rgba(255,255,255,0.25);
    display: flex; align-items: center; justify-content: center;
  }
  .brand-name {
    font-weight: 600; font-size: 34px; color: var(--blue-deep);
    letter-spacing: 1px; text-transform: lowercase;
  }
  .person { position: absolute; top: 272px; width: 100%; text-align: center; color: var(--white); }
  .person__name { font-size: 27px; font-weight: 300; letter-spacing: 0.5px; }
  .person__name strong { font-weight: 600; }
  .person__title { font-size: 11px; font-weight: 300; margin-top: 4px; opacity: 0.9; }
  .web-band {
    position: absolute; bottom: 0; width: 100%; height: 128px;
    background: var(--band);
    display: flex; align-items: center; justify-content: center;
  }
  .web-band__url { font-size: 17px; color: var(--blue-mid); letter-spacing: 0.3px; }

  /* back */
  .location-map {
    position: absolute; left: 55px; top: 48px;
    width: 230px; height: 230px; border-radius: 50%;
    background: radial-gradient(circle at 45% 40%, #f2f4f7 0%, var(--map-tone) 100%);
    box-shadow: 0 0 0 8px rgba(255,255,255,0.25);
  }
  .scallop { position: absolute; left: 0; top: 372px; width: 340px; height: 40px; display: block; }
  .contact {
    position: absolute; left: 0; top: 410px; width: 100%; height: 170px;
    background: var(--white);
    padding: 22px 30px 0;
    list-style: none;
  }
  .contact__item {
    display: flex; align-items: center; gap: 14px;
    font-size: 13px; color: var(--blue-mid); margin-bottom: 22px;
  }
  .contact__icon { width: 16px; height: 16px; flex: none; }
</style>
</head>
<body>

<section class="card card--front" aria-label="Card front">
  <div class="brand-disc"><span class="brand-name">velmit</span></div>
  <div class="person">
    <p class="person__name">Daniel <strong>Marsh</strong></p>
    <p class="person__title">CEO - velmit pools</p>
  </div>
  <div class="web-band"><span class="web-band__url">www.velmitpools.example</span></div>
</section>

<section class="card card--back" aria-label="Card back">
  <div class="location-map" role="img" aria-label="Street map showing the office location"></div>
  <svg class="scallop" viewBox="0 0 340 40" preserveAspectRatio="none" aria-hidden="true">
    <path fill="#ffffff" d="M0,40 L0,22 A28.33,18 0 0 1 56.67,22 A28.33,18 0 0 1 113.33,22 A28.33,18 0 0 1 170,22 A28.33,18 0 0 1 226.67,22 A28.33,18 0 0 1 283.33,22 A28.33,18 0 0 1 340,22 L340,40 Z"/>
  </svg>
  <ul class="contact">
    <li class="contact__item">
      <svg class="contact__icon" viewBox="0 0 16 16" aria-hidden="true"><path fill="none" stroke="#3176b5" stroke-width="1.5" d="M8 15s5-5.2 5-8.8A5 5 0 0 0 3 6.2C3 9.8 8 15 8 15z"/><circle cx="8" cy="6.3" r="1.8" fill="#3176b5"/></svg>
      <span>1820 Harbor Lane Sunvale, CA 90000</span>
    </li>
    <li class="contact__item">
      <svg class="contact__icon" viewBox="0 0 16 16" aria-hidden="true"><rect x="1.5" y="3.5" width="13" height="9" fill="none" stroke="#3176b5" stroke-width="1.5"/><path d="M1.5 3.5 8 9l6.5-5.5" fill="none" stroke="#3176b5" stroke-width="1.5"/></svg>
      <span>dan@velmitpools.example</span>
    </li>
    <li class="contact__item">
      <svg class="contact__icon" viewBox="0 0 16 16" aria-hidden="true"><path fill="#3176b5" d="M4.2 1.5 6.3 4 5 5.6c.8 1.9 2.4 3.5 4.4 4.4L11 8.7l2.5 2.1-1.2 2.6c-.3.5-.8.7-1.4.6C6.3 13.2 2.8 9.7 2 5.1c-.1-.6.1-1.1.6-1.4z"/></svg>
      <span>555-014-2290</span>
    </li>
  </ul>
</section>

</body>
</html>
```